Financial planning organization needs an PLVK postcard inviting 55+ community to attend a monthly...

We need a standard postcard to use for our monthly tea and financial discussion at a senior living community. The tea features an informal discussion with a Licensed Money Counselor to address the news of the day as well as personal financial questions. We would like to see designs that use graphics rather than photos. In earlier attempts we found the photos of people just not working. Final design should be clean and simple.

Target Market(s)

55+ Community (senior citizens)

Industry/Entity Type

Financial Planning

Font styles to use
Serif
Sans Serif

Requirements
Must have
• PLVK formatting
• Graphics/ graphic heavy

```html
<!DOCTYPE html>
<html lang="en">
<head>
<meta charset="utf-8">
<title>Tea with Ned – Postcard</title>
<link href="https://fonts.googleapis.com/css2?family=Lato:ital,wght@0,300;0,400;0,700;1,400&family=Montserrat:ital,wght@0,400;1,700&family=Playfair+Display:ital,wght@1,400&display=swap" rel="stylesheet">
<style>
  :root {
    --bg: #e9e9ea;
    --card: #f4f4f3;
    --navy: #27308c;
    --band: #4249bd;
    --grey-text: #4a4d55;
    --title: #6e5132;
    --frame: #a89a86;
    --rule: #4a4d55;
    --line: #6b6d73;
  }
  * { margin: 0; padding: 0; box-sizing: border-box; }
  html, body { width: 1200px; height: 960px; overflow: hidden; }
  body {
    background: var(--bg);
    font-family: "Lato", sans-serif;
    display: flex;
    align-items: center;
    justify-content: center;
    gap: 40px;
  }
  .postcard {
    position: relative;
    width: 560px;
    height: 396px;
    background: var(--card);
    overflow: hidden;
    box-shadow: 0 6px 18px rgba(0,0,0,0.12);
  }

  /* Front */
  .front-photo {
    position: absolute;
    inset: 0;
    background: linear-gradient(100deg, #eceeee 0%, #f7f8f8 40%, #eef0f1 62%, #e4ecec 100%);
  }
  .mug-area {
    position: absolute;
    left: 52px; top: 78px;
    width: 226px; height: 296px;
    border-radius: 10px 10px 30px 30px;
    background: linear-gradient(90deg, #ecebe6 0%, #fbfbf9 45%, #f1f0ec 100%);
  }
  .event-title {
    position: absolute;
    left: 122px; top: 148px;
    width: 102px; height: 172px;
    border: 1.5px solid var(--frame);
    display: flex;
    flex-direction: column;
    align-items: center;
    justify-content: center;
    color: var(--title);
    line-height: 1;
  }
  .event-title .title-word {
    font-family: "Playfair Display", serif;
    font-style: italic;
    font-size: 40px;
  }
  .event-title .title-join {
    font-family: "Lato", sans-serif;
    font-weight: 300;
    font-size: 22px;
    margin: 4px 0 2px;
  }
  .front-panel {
    position: absolute;
    top: 0; right: 0;
    width: 270px; height: 100%;
    background: linear-gradient(160deg, rgba(205,225,222,0.55), rgba(199,220,216,0.85));
    clip-path: polygon(30% 0, 100% 0, 100% 100%, 0 100%, 0 38%);
  }
  .front-info {
    position: absolute;
    left: 318px; top: 106px;
    width: 226px;
  }
  .brand {
    font-family: "Lato", sans-serif;
    font-weight: 400;
    color: var(--navy);
    display: flex;
    align-items: center;
    gap: 7px;
    font-size: 16px;
    letter-spacing: 1px;
    line-height: 1;
    white-space: nowrap;
    margin-bottom: 24px;
  }
  .brand-mark {
    width: 13px; height: 13px;
    border-radius: 50%;
    background: var(--navy);
    flex: none;
  }
  .event-day { font-weight: 700; color: var(--grey-text); font-size: 16px; letter-spacing: 0.5px; }
  .event-date { color: var(--navy); font-size: 22px; line-height: 1.25; }
  .event-time { font-weight: 700; color: var(--grey-text); font-size: 15px; }
  .event-place { color: var(--navy); font-size: 22px; line-height: 1.35; padding-bottom: 6px; border-bottom: 2px solid var(--rule); width: 180px; }
  .event-note { font-style: italic; color: var(--grey-text); font-size: 12.5px; line-height: 1.35; margin-top: 8px; width: 180px; }

  /* Back */
  .back-left {
    position: absolute;
    top: 0; left: 0;
    width: 300px; height: 100%;
    background: #e7e7e6;
    clip-path: polygon(0 0, 100% 0, 78% 100%, 0 100%);
  }
  .back-band {
    position: absolute;
    top: 0; left: 86px;
    width: 168px; height: 64px;
    background: var(--band);
  }
  .portrait {
    position: absolute;
    top: 22px; left: 96px;
    width: 148px; height: 148px;
    border-radius: 50%;
    border: 4px solid #ffffff;
    background: radial-gradient(circle at 45% 45%, #c9a9a0 0%, #7a8a6a 55%, #4b5a3e 100%);
  }
  .back-copy {
    position: absolute;
    left: 24px; top: 190px;
    width: 290px;
    text-align: center;
    font-family: "Montserrat", sans-serif;
  }
  .tagline { font-style: italic; font-weight: 700; color: var(--navy); font-size: 11px; margin-bottom: 6px; white-space: nowrap; }
  .bio { color: var(--grey-text); font-size: 8.5px; line-height: 1.35; }
  .back-brand {
    position: absolute;
    left: 88px; top: 300px;
    font-size: 17px;
  }
  .address-lines {
    position: absolute;
    left: 340px; top: 170px;
    width: 190px;
  }
  .address-lines span {
    display: block;
    height: 1px;
    background: var(--line);
    margin-bottom: 26px;
  }
</style>
</head>
<body>
  <section class="postcard postcard-front">
    <div class="front-photo" role="img" aria-label="Photo of a white mug on a bright windowsill"></div>
    <div class="mug-area" role="img" aria-label="White mug"></div>
    <h1 class="event-title">
      <span class="title-word">Tea</span>
      <span class="title-join">with</span>
      <span class="title-word">Ned</span>
    </h1>
    <div class="front-panel"></div>
    <div class="front-info">
      <div class="brand"><span class="brand-mark"></span>HALVORSEN ADVISORS</div>
      <p class="event-day">THURSDAY</p>
      <p class="event-date">August 15th</p>
      <p class="event-time">@ 3:00PM</p>
      <p class="event-place">Linden Hall</p>
      <p class="event-note">Tea, lemonade and sweets will be served discussion and open forum.</p>
    </div>
  </section>

  <section class="postcard postcard-back">
    <div class="back-left"></div>
    <div class="back-band"></div>
    <div class="portrait" role="img" aria-label="Portrait photo of Ned Halvorsen"></div>
    <div class="back-copy">
      <p class="tagline">A Licensed Money Counselor™ you can trust.</p>
      <p class="bio">Ned Halvorsen is a LICENSED MONEY COUNSELOR™ and Fiduciary specializing in asset management of IRA, retirement, investment, and trust accounts. Halvorsen Advisors, LLC is an independent Registered Investment Advisor with a low cost, commission-free business model.</p>
    </div>
    <div class="brand back-brand"><span class="brand-mark"></span>HALVORSEN ADVISORS</div>
    <div class="address-lines"><span></span><span></span><span></span></div>
  </section>
</body>
</html>
```